Jolly Paws Business Card Update

I have a business card which I love. I want to keep the same logo, colours, font and style. I want to upgrade the scripting and remove some elements and add others.
On the front side under Services - remove the existing wording and insert - Providing individual coaching strategies to create happy, healthy and social canine companions
Under Rebecca Thornley amend the current wording to read: Qualified in Dog Behavioural Training, Natural Animal Healthcare and Animal Health Science
On the reverse side to remove the web address.

```html
<!DOCTYPE html>
<html lang="en">
<head>
<meta charset="utf-8">
<title>Jolly Paws Business Card</title>
<link rel="stylesheet" href="https://fonts.googleapis.com/css2?family=Arimo:wght@400;700&display=swap">
<style>
  :root {
    --backdrop: #e4e4e4;
    --blue-light: #0a98d6;
    --blue-deep: #1d3c98;
    --red-bright: #e21f26;
    --red-dark: #5a0c10;
    --cream: #efe6c8;
    --ink: #1a1a1a;
  }
  * { margin: 0; padding: 0; box-sizing: border-box; }
  html, body {
    width: 1200px; height: 800px; overflow: hidden;
    background: var(--backdrop);
    font-family: "Arimo", Arial, sans-serif;
  }
  .sheet {
    width: 1200px; height: 800px;
    display: flex; align-items: center; justify-content: center; gap: 30px;
  }
  .card {
    position: relative; width: 570px; height: 326px;
    border-radius: 42px; overflow: hidden;
    box-shadow: 0 10px 24px rgba(0,0,0,0.22);
  }
  .card-bg { position: absolute; inset: 0; width: 100%; height: 100%; }
  .card-text { position: absolute; color: var(--cream); }

  /* front */
  .brand-name {
    left: 0; right: 0; top: 196px; text-align: center;
    font-size: 40px; font-weight: 700; letter-spacing: 1px;
  }
  .tagline {
    left: 0; right: 0; top: 244px; text-align: center;
    font-size: 16px; letter-spacing: 1px;
  }

  /* back */
  .mini-brand {
    left: 20px; width: 120px; top: 142px; text-align: center;
    font-size: 13px; font-weight: 700;
  }
  .services { left: 172px; top: 44px; width: 380px; font-weight: 700; }
  .services-title { font-size: 16px; margin-bottom: 8px; letter-spacing: 0.5px; }
  .services-body { font-size: 15px; line-height: 1.3; }
  .mission {
    left: 0; right: 0; top: 178px; height: 14px; line-height: 14px;
    text-align: center; font-size: 10.5px; color: var(--ink);
  }
  .person { right: 276px; top: 204px; text-align: right; }
  .person-name { font-size: 22px; margin-bottom: 5px; }
  .person-credentials { font-size: 12px; line-height: 1.3; }
  .contact { left: 312px; top: 210px; font-size: 15px; line-height: 1.55; }
  .contact-row { display: flex; align-items: center; gap: 7px; }
  .contact-icon { width: 14px; height: 14px; flex: none; }
</style>
</head>
<body>
<main class="sheet">

  <section class="card card-front" aria-label="Card front">
    <svg class="card-bg" viewBox="0 0 570 326" aria-hidden="true">
      <defs>
        <linearGradient id="front-blue" x1="0" y1="0" x2="0.3" y2="1">
          <stop offset="0" stop-color="#0a98d6"/>
          <stop offset="1" stop-color="#1d3c98"/>
        </linearGradient>
        <linearGradient id="front-red" x1="0" y1="0" x2="1" y2="0">
          <stop offset="0" stop-color="#5a0c10"/>
          <stop offset="0.5" stop-color="#e21f26"/>
          <stop offset="1" stop-color="#6a0e12"/>
        </linearGradient>
      </defs>
      <rect width="570" height="326" fill="url(#front-blue)"/>
      <path d="M40 326 Q320 300 570 232 L570 326 Z" fill="url(#front-red)"/>
      <path d="M40 326 Q320 300 570 232" fill="none" stroke="#efe6c8" stroke-width="3"/>
      <circle cx="285" cy="105" r="58" fill="#efe6c8" stroke="#b2161c" stroke-width="9"/>
    </svg>
    <div class="card-text brand-name">JOLLY PAWS</div>
    <div class="card-text tagline">HAPPY DOGS, HAPPY OWNERS</div>
  </section>

  <section class="card card-back" aria-label="Card back">
    <svg class="card-bg" viewBox="0 0 570 326" aria-hidden="true">
      <defs>
        <linearGradient id="back-blue" x1="0" y1="0" x2="0" y2="1">
          <stop offset="0" stop-color="#0a98d6"/>
          <stop offset="1" stop-color="#1650b0"/>
        </linearGradient>
        <linearGradient id="back-red" x1="0" y1="0" x2="1" y2="0">
          <stop offset="0" stop-color="#5a0c10"/>
          <stop offset="0.45" stop-color="#e21f26"/>
          <stop offset="1" stop-color="#5a0c10"/>
        </linearGradient>
      </defs>
      <rect width="570" height="180" fill="url(#back-blue)"/>
      <rect y="178" width="570" height="14" fill="#efe6c8"/>
      <rect y="192" width="570" height="134" fill="url(#back-red)"/>
      <circle cx="80" cy="86" r="46" fill="#efe6c8" stroke="#b2161c" stroke-width="7"/>
      <line x1="155" y1="40" x2="155" y2="160" stroke="#efe6c8" stroke-width="1"/>
      <line x1="300" y1="206" x2="300" y2="292" stroke="#efe6c8" stroke-width="1"/>
    </svg>

    <div class="card-text mini-brand">Jolly Paws</div>

    <div class="card-text services">
      <div class="services-title">SERVICES</div>
      <div class="services-body">Providing individual coaching<br>strategies to create happy, healthy<br>and social canine companions</div>
    </div>

    <div class="card-text mission">Promoting communication and connection between dogs and their families</div>

    <div class="card-text person">
      <div class="person-name">Rebecca Thornley</div>
      <div class="person-credentials">Qualified in Dog Behavioural Training,<br>Natural Animal Healthcare and Animal<br>Health Science</div>
    </div>

    <div class="card-text contact">
      <div class="contact-row">
        <svg class="contact-icon" viewBox="0 0 14 14" aria-hidden="true">
          <circle cx="7" cy="7" r="7" fill="#efe6c8"/>
          <rect x="4.5" y="2.8" width="5" height="8.4" rx="1" fill="#b2161c"/>
        </svg>
        <span>0400 217 386</span>
      </div>
      <div class="contact-row">
        <svg class="contact-icon" viewBox="0 0 14 14" aria-hidden="true">
          <circle cx="7" cy="7" r="7" fill="#efe6c8"/>
          <rect x="3.5" y="4.5" width="7" height="5" fill="#b2161c"/>
          <path d="M3.5 4.5 L7 7.5 L10.5 4.5" fill="none" stroke="#efe6c8" stroke-width="0.8"/>
        </svg>
        <span>jollypaws1@example.com</span>
      </div>
    </div>
  </section>

</main>
</body>
</html>
```